Business Card Design Project

We need a logo design for a new company based in Southern California called "Norvale Security Services, Inc." We install security and camera systems for homeowners and business, to protect their assets.
Updates

Project Deadline Extended
Reason: LOGO Design completes in eight days. Would like that design decided before we finish the business cards. Thanks...

Target Market(s)

Homeowners and business owners looking for additional protection of their assets.

Industry/Entity Type

Security

Font styles to use
Serif

Requirements
Must have
• Company Name
Office# 626-472-3615
Service# 626-472-3616
email: NorvaleSecurity@brimwell.net
address: 48620 Thorncrest Lane Brookhaven, CA 91704
Nice to have
• Serving Southern California

```html
<!DOCTYPE html>
<html lang="en">
<head>
<meta charset="utf-8">
<title>Norvale Security Services – Business Card</title>
<link rel="stylesheet" href="https://fonts.googleapis.com/css2?family=Open+Sans:wght@400;600;700&display=swap">
<style>
  :root {
    --backdrop: #1c1c1e;
    --card-white: #f7f7f5;
    --slate: #58595b;
    --sky: #1a9fdb;
    --ink: #3a3a3c;
  }
  * { margin: 0; padding: 0; box-sizing: border-box; }
  html, body {
    width: 1200px;
    height: 757px;
    overflow: hidden;
    background: var(--backdrop);
    font-family: "Open Sans", Arial, sans-serif;
  }
  .card {
    position: absolute;
    left: 150px;
    top: 121px;
    width: 900px;
    height: 514px;
    background: var(--card-white);
    overflow: hidden;
  }
  .card-shapes {
    position: absolute;
    inset: 0;
  }
  .holder {
    position: absolute;
    left: 58px;
    top: 58px;
  }
  .holder-name {
    font-size: 27px;
    font-weight: 700;
    color: var(--ink);
    line-height: 1.1;
  }
  .holder-title {
    font-size: 19px;
    font-weight: 400;
    color: var(--sky);
    line-height: 1.3;
  }
  .contacts {
    position: absolute;
    left: 58px;
    top: 160px;
    list-style: none;
  }
  .contact {
    display: flex;
    align-items: center;
    height: 40px;
    font-size: 18px;
    color: var(--ink);
    letter-spacing: 0.2px;
    white-space: nowrap;
  }
  .contact svg {
    width: 18px;
    height: 18px;
    margin-right: 20px;
    fill: var(--sky);
    flex: none;
  }
  .brand {
    position: absolute;
    left: 330px;
    top: 52px;
    display: flex;
    align-items: center;
  }
  .brand-dot {
    width: 38px;
    height: 38px;
    border-radius: 50%;
    background: var(--sky);
    margin-right: 22px;
  }
  .brand-name {
    font-size: 26px;
    font-weight: 600;
    color: var(--sky);
    white-space: nowrap;
  }
</style>
</head>
<body>
  <main class="card">
    <svg class="card-shapes" width="900" height="514" viewBox="0 0 900 514" aria-hidden="true">
      <polygon points="175,0 900,0 900,455 845,462" fill="var(--slate)"/>
      <rect x="0" y="0" width="900" height="7" fill="var(--sky)"/>
      <polygon points="845,462 900,455 900,464 848,471" fill="var(--sky)"/>
      <polygon points="540,205 845,462 330,505" fill="var(--sky)"/>
    </svg>

    <div class="brand">
      <span class="brand-dot"></span>
      <span class="brand-name">Norvale Security Services, Inc.</span>
    </div>

    <header class="holder">
      <h1 class="holder-name">Dale Corwin</h1>
      <p class="holder-title">Manager</p>
    </header>

    <ul class="contacts">
      <li class="contact">
        <svg viewBox="0 0 24 24"><path d="M6.6 10.8a15.1 15.1 0 0 0 6.6 6.6l2.2-2.2c.3-.3.7-.4 1-.2 1.1.4 2.3.6 3.6.6.6 0 1 .4 1 1V20c0 .6-.4 1-1 1A17 17 0 0 1 3 4c0-.6.4-1 1-1h3.5c.6 0 1 .4 1 1 0 1.3.2 2.5.6 3.6.1.3 0 .7-.2 1z"/></svg>
        626-472-3615
      </li>
      <li class="contact">
        <svg viewBox="0 0 24 24"><path d="M6.6 10.8a15.1 15.1 0 0 0 6.6 6.6l2.2-2.2c.3-.3.7-.4 1-.2 1.1.4 2.3.6 3.6.6.6 0 1 .4 1 1V20c0 .6-.4 1-1 1A17 17 0 0 1 3 4c0-.6.4-1 1-1h3.5c.6 0 1 .4 1 1 0 1.3.2 2.5.6 3.6.1.3 0 .7-.2 1z"/></svg>
        626-472-3616
      </li>
      <li class="contact">
        <svg viewBox="0 0 24 24"><path d="M2 5h20v2l-10 6L2 7z M2 9l10 6 10-6v10H2z"/></svg>
        NorvaleSecurity@brimwell.net
      </li>
      <li class="contact">
        <svg viewBox="0 0 24 24"><path d="M12 2a7 7 0 0 0-7 7c0 5.2 7 13 7 13s7-7.8 7-13a7 7 0 0 0-7-7zm0 9.5A2.5 2.5 0 1 1 12 6.5a2.5 2.5 0 0 1 0 5z"/></svg>
        48620 Thorncrest Lane Brookhaven
      </li>
    </ul>
  </main>
</body>
</html>
```